Box design for tovalunex

TovaLunex ackage design development brief.
Technical specification:
Package measurements – 200x200x40mm or 150x150x60mm (see pictures of an example below).
Design only for outer layer, no printing inside.
As the box itself is the main product, the aim of this design is to be outstanding – modern, clean,
sophisticated, attractive, memorable and providing WoW-effect to the consumer.

Industry/Entity Type

Printing

```html
<!DOCTYPE html>
<html lang="en">
<head>
<meta charset="utf-8">
<title>TovaLunex box dieline</title>
<link rel="stylesheet" href="https://fonts.googleapis.com/css2?family=Raleway:wght@300&display=swap">
<style>
  :root {
    --paper: #ffffff;
    --rose-deep: #a9566c;
    --rose-mid: #d194a4;
    --rose-light: #f1d5dc;
    --rose-glow: #ecc3ce;
    --mark-faint: rgba(255, 255, 255, 0.6);
    --ink-grey: #9a9a9a;
    --cut-line: #2a2a2a;
  }
  html, body {
    margin: 0;
    padding: 0;
    overflow: hidden;
    background: var(--paper);
  }
  .dieline {
    position: relative;
    width: 1200px;
    height: 1189px;
    background: var(--paper);
  }
  .panel {
    position: absolute;
    box-sizing: border-box;
    border: 1px solid var(--cut-line);
  }
  .flap-top, .flap-bottom {
    display: flex;
    align-items: center;
    justify-content: center;
  }
  .flap-top {
    left: 197px; top: 29px; width: 806px; height: 164px;
    background: linear-gradient(to bottom, var(--rose-deep), var(--rose-mid) 40%, var(--rose-light));
  }
  .flap-bottom {
    left: 197px; top: 1003px; width: 806px; height: 164px;
    background: linear-gradient(to top, var(--rose-deep), var(--rose-mid) 40%, var(--rose-light));
  }
  .flap-mark {
    margin: 0;
    font-family: "Raleway", sans-serif;
    font-weight: 300;
    font-size: 26px;
    letter-spacing: 2px;
    color: var(--mark-faint);
  }
  .flap-left {
    left: 34px; top: 192px; width: 164px; height: 812px;
    background: linear-gradient(to right, var(--rose-deep), var(--rose-mid) 45%, var(--rose-light));
  }
  .flap-right {
    left: 1002px; top: 192px; width: 164px; height: 812px;
    background: linear-gradient(to left, var(--rose-deep), var(--rose-mid) 45%, var(--rose-light));
  }
  .edge-pattern {
    position: absolute;
    top: 0; bottom: 0;
    width: 30px;
  }
  .flap-left .edge-pattern {
    left: 0;
    background: linear-gradient(to right, rgba(255,255,255,0.3), rgba(255,255,255,0));
  }
  .flap-right .edge-pattern {
    right: 0;
    background: linear-gradient(to left, rgba(255,255,255,0.3), rgba(255,255,255,0));
  }
  .lid-face {
    left: 197px; top: 192px; width: 806px; height: 812px;
    background: var(--paper);
    box-shadow: inset 0 0 70px 20px var(--rose-glow);
  }
  .brand-square {
    position: absolute;
    left: 545px;
    top: 490px;
    width: 110px;
    height: 110px;
    background: var(--rose-deep);
  }
  .brand-name {
    position: absolute;
    left: 0; right: 0;
    top: 660px;
    margin: 0;
    text-align: center;
    font-family: "Raleway", sans-serif;
    font-weight: 300;
    font-size: 84px;
    letter-spacing: 4px;
    color: var(--ink-grey);
  }
</style>
</head>
<body>
  <main class="dieline">
    <div class="panel flap-top"><p class="flap-mark">TOVALUNEX</p></div>
    <div class="panel flap-left">
      <div class="edge-pattern" role="img" aria-label="Light zigzag edge pattern"></div>
    </div>
    <div class="panel lid-face"></div>
    <div class="panel flap-right">
      <div class="edge-pattern" role="img" aria-label="Light zigzag edge pattern"></div>
    </div>
    <div class="panel flap-bottom"><p class="flap-mark">TOVALUNEX</p></div>
    <div class="brand-square" aria-hidden="true"></div>
    <h1 class="brand-name">TOVALUNEX</h1>
  </main>
</body>
</html>
```